Full printing package for Fadeel Trading & Maint. Co. Ltd
Business card, email signature, A4 folder & stationary
Full printing package for Fadeel Trading & Maint. Co. Ltd -
Tariq Mardini
Executive Manager
P.O.Box 4582, Riyadh 13872 Kingdom of Saudi Arabia
t.mardini@fadeelco-ksa.com
www.fadeelco-ksa.com
I need two designs for the business card: 1.front side to have name & title in both arabic & English ( address in English only) and on the back side logo & website. 2. One side name ,company name & title in arabic ( address only english) back side name ,company name & title in english. For A4 envelope,letter head,email signature & folder to use same address as business card.

```html
<!DOCTYPE html>
<html lang="en">
<head>
<meta charset="utf-8">
<title>Fadeel Trading &amp; Maint. Co. Ltd – Business Card Options</title>
<link href="https://fonts.googleapis.com/css2?family=Lato:ital,wght@0,400;0,700;1,400&family=Noto+Naskh+Arabic:wght@400;500&display=swap" rel="stylesheet">
<style>
  :root {
    --sheet: #f1f1f1;
    --coral: #dc6a4e;
    --slate: #4e6283;
    --ink: #3b3b3b;
    --grey: #666666;
    --white: #ffffff;
  }
  * { box-sizing: border-box; margin: 0; padding: 0; }
  html, body { width: 1200px; height: 806px; overflow: hidden; background: var(--sheet); }
  .sheet { position: relative; width: 1200px; height: 806px; font-family: "Lato", Arial, sans-serif; color: var(--ink); }

  .card {
    position: absolute; width: 511px; height: 293px;
    background: linear-gradient(90deg, var(--coral) 0 50%, var(--slate) 50% 100%);
    padding: 16px;
  }
  .card-face { position: relative; width: 100%; height: 100%; background: var(--white); text-align: center; }

  .front-a { left: 77px; top: 43px; }
  .front-b { left: 643px; top: 43px; }
  .back-a  { left: 77px; top: 408px; }
  .back-b  { left: 643px; top: 408px; }

  .caption {
    position: absolute; width: 511px; text-align: center;
    font-size: 19px; letter-spacing: 2.5px; font-variant: small-caps; color: #333;
  }
  .caption.row-1 { top: 344px; }
  .caption.row-2 { top: 712px; }
  .caption.col-a { left: 77px; }
  .caption.col-b { left: 643px; }

  .name-line { position: absolute; left: 0; right: 0; font-size: 17px; }
  .name-line .person { color: var(--coral); font-style: italic; }
  .name-line .role { color: var(--ink); }

  .ar { font-family: "Noto Naskh Arabic", serif; direction: rtl; position: absolute; left: 0; right: 0; }
  .ar-name { font-size: 23px; color: var(--ink); }
  .ar-role { font-size: 16px; color: var(--grey); }
  .ar-company { font-size: 23px; color: var(--coral); top: 18px; font-weight: 400; white-space: nowrap; }

  .contact { position: absolute; left: 0; right: 0; font-size: 9.5px; color: var(--grey); line-height: 1; }
  .contact span { display: inline-flex; align-items: center; gap: 4px; margin: 0 4px; }
  .contact svg { width: 10px; height: 10px; fill: var(--coral); }

  .company-name {
    position: absolute; left: 0; right: 0;
    font-size: 24px; font-weight: 400; color: var(--ink); letter-spacing: 0.3px;
  }

  .web { position: absolute; left: 0; right: 0; font-size: 15px; color: var(--coral); font-style: italic; }
</style>
</head>
<body>
<main class="sheet">

  <!-- Front option A -->
  <section class="card front-a">
    <div class="card-face">
      <p class="name-line" style="top:26px"><span class="person">Tariq Mardini</span> | <span class="role">Executive Manager</span></p>
      <p class="ar ar-name" style="top:78px">طارق مارديني</p>
      <p class="ar ar-role" style="top:116px">المدير التنفيذي</p>
      <p class="contact" style="top:186px"><span><svg viewBox="0 0 10 10"><path d="M5 1 1 5h1.5v4h2V6.5h1V9h2V5H9z"/></svg>P.O.Box 4582, Riyadh 13872 Kingdom of Saudi Arabia</span></p>
      <p class="contact" style="top:205px"><span><svg viewBox="0 0 10 10"><path d="M1 2h8v6H1zm0 0 4 3.5L9 2"/></svg>t.mardini@fadeelco-ksa.com</span><span><svg viewBox="0 0 10 10"><circle cx="5" cy="5" r="4"/></svg>www.fadeelco-ksa.com</span></p>
      <p class="contact" style="top:224px"><span><svg viewBox="0 0 10 10"><path d="M2 1h2l1 2.5-1.3 1a5 5 0 0 0 2 2l1-1.3L9 6v2a1 1 0 0 1-1 1C4.5 9 1 5.5 1 2a1 1 0 0 1 1-1z"/></svg>+966-1-4820150/250/350</span><span><svg viewBox="0 0 10 10"><rect x="3" y="1" width="4" height="8" rx="1"/></svg>+966-559283614</span><span><svg viewBox="0 0 10 10"><path d="M2 4h6v5H2zM3 1h4v3H3z"/></svg>+966-1-4829077</span></p>
    </div>
  </section>

  <!-- Front option B -->
  <section class="card front-b">
    <div class="card-face">
      <p class="ar ar-company">شركة الفضيل للمقاولات والتجارة والصيانة المحدودة</p>
      <p class="ar ar-name" style="top:78px">طارق مارديني</p>
      <p class="ar ar-role" style="top:116px">المدير التنفيذي</p>
      <p class="contact" style="top:186px"><span><svg viewBox="0 0 10 10"><path d="M5 1 1 5h1.5v4h2V6.5h1V9h2V5H9z"/></svg>P.O.Box 4582, Riyadh 13872 Kingdom of Saudi Arabia</span></p>
      <p class="contact" style="top:205px"><span><svg viewBox="0 0 10 10"><path d="M1 2h8v6H1zm0 0 4 3.5L9 2"/></svg>t.mardini@fadeelco-ksa.com</span><span><svg viewBox="0 0 10 10"><circle cx="5" cy="5" r="4"/></svg>www.fadeelco-ksa.com</span></p>
      <p class="contact" style="top:224px"><span><svg viewBox="0 0 10 10"><path d="M2 1h2l1 2.5-1.3 1a5 5 0 0 0 2 2l1-1.3L9 6v2a1 1 0 0 1-1 1C4.5 9 1 5.5 1 2a1 1 0 0 1 1-1z"/></svg>+966-1-4820150/250/350</span><span><svg viewBox="0 0 10 10"><rect x="3" y="1" width="4" height="8" rx="1"/></svg>+966-559283614</span><span><svg viewBox="0 0 10 10"><path d="M2 4h6v5H2zM3 1h4v3H3z"/></svg>+966-1-4829077</span></p>
    </div>
  </section>

  <!-- Back option A -->
  <section class="card back-a">
    <div class="card-face">
      <p class="company-name" style="top:112px">Fadeel Trading &amp; Maint. Co. Ltd</p>
      <p class="web" style="top:220px">www.fadeelco-ksa.com</p>
    </div>
  </section>

  <!-- Back option B -->
  <section class="card back-b">
    <div class="card-face">
      <p class="company-name" style="top:112px">Fadeel Trading &amp; Maint. Co. Ltd</p>
      <p class="name-line" style="top:218px"><span class="person">Tariq Mardini</span> | <span class="role">Executive Manager</span></p>
    </div>
  </section>

  <p class="caption row-1 col-a">Business Card Front Option A</p>
  <p class="caption row-1 col-b">Business Card Front Option B</p>
  <p class="caption row-2 col-a">Business Card Back Option A</p>
  <p class="caption row-2 col-b">Business Card Back Option B</p>

</main>
</body>
</html>
```